New Stationary for our business

We are a gift business and would like to create a new corporate image with new stationary and design.

We would like a Classic Corporate look with a touch of Flair.

We would need:
Envelopes
Letter Head
Business Cards
With Comp Slips
Note Pads
Etc...

Our details are:

Basket Haven Pty Ltd
518 Tallow Street, Fernmead, Victoria, 3071
1800 742 918
www.baskethaven-demo.com.au
sales@baskethaven-demo.com.au

ABN: 58 603 214 796

Target Market(s)

Corporate Look

Industry/Entity Type

Marketing

Contact Information for Business Card

Basket Haven Pty Ltd
1800 742 918
518 Tallow Street
Fernmead 3071
Victoria Australia

Darren Pelluso - Managing Director
darren.pelluso@baskethaven-demo.com.au
0413 587 120

Logo Text

Basket Haven - The Gift Specialists

Colors

Designer to choose colors to be used in the design.

Requirements
Must have
• Look and Feel upmarket and exclusive

```html
<!DOCTYPE html>
<html lang="en">
<head>
<meta charset="utf-8">
<title>Basket Haven — Business Cards</title>
<link rel="stylesheet" href="https://fonts.googleapis.com/css2?family=Tinos:wght@400&family=Arimo:wght@400&display=swap">
<style>
  :root {
    --backdrop: #e4e4e2;
    --navy: #173a6c;
    --paper: #ffffff;
    --ink: #1e1e1e;
    --muted: #8c8c8c;
    --on-navy: #ffffff;
  }
  * { box-sizing: border-box; margin: 0; padding: 0; }
  html, body { width: 1200px; height: 800px; overflow: hidden; }
  body {
    background: var(--backdrop);
    position: relative;
    font-family: "Arimo", Arial, sans-serif;
  }
  .card {
    position: absolute;
    top: 246px;
    width: 540px;
    height: 308px;
    box-shadow: 0 6px 18px rgba(0,0,0,0.18);
  }
  .card--back { left: 40px; background: var(--navy); color: var(--on-navy); }
  .card--front { left: 620px; background: var(--paper); color: var(--ink); }

  .brand-name {
    font-family: "Tinos", "Times New Roman", serif;
    font-weight: 400;
    text-transform: uppercase;
    letter-spacing: 1px;
    text-align: center;
    white-space: nowrap;
  }
  .card--back .brand-name {
    position: absolute; left: 0; right: 0; top: 100px;
    font-size: 46px; color: var(--on-navy);
  }
  .card--back .abn {
    position: absolute; left: 0; right: 0; top: 200px;
    text-align: center; font-size: 13px; letter-spacing: 0.5px;
  }
  .card--front .brand-name {
    position: absolute; left: 0; right: 0; top: 40px;
    font-size: 40px; color: var(--navy);
  }
  .person {
    position: absolute; left: 0; right: 0; top: 128px; text-align: center;
  }
  .person__name {
    font-family: "Tinos", "Times New Roman", serif;
    font-size: 27px; color: var(--ink);
  }
  .person__role {
    font-size: 15px; letter-spacing: 0.5px; text-transform: uppercase; margin-top: 2px;
  }
  .contact {
    position: absolute; left: 0; right: 0; top: 232px;
    text-align: center; font-size: 13px; line-height: 1.6; white-space: nowrap;
  }
  .contact .sep { color: var(--navy); margin: 0 7px; font-weight: 700; }
</style>
</head>
<body>
  <section class="card card--back" aria-label="Business card back">
    <div class="brand-name">Basket Haven</div>
    <p class="abn">ABN: 58 603 214 796</p>
  </section>

  <section class="card card--front" aria-label="Business card front">
    <div class="brand-name">Basket Haven</div>
    <div class="person">
      <p class="person__name">Margot Ellery</p>
      <p class="person__role">President</p>
    </div>
    <div class="contact">
      <p>www.baskethaven-demo.com.au<span class="sep">|</span>1800 742 918<span class="sep">|</span>sales@baskethaven-demo.com.au</p>
      <p>518 Tallow Street, Fernmead, Victoria, 3071</p>
    </div>
  </section>
</body>
</html>
```